Maplers Report Design for Senior Care REIT

We have pulled high-level summary information from a Mapler Report, and compiled what we care about into the attached document. We would like you to take the information in the document and create a visual sheet, flyer, or slide deck (option to best layout based on info and creative vision). This should be QVN branded (logo attached) and should reflect design elements and vibes that you see on (qvnreit.example). This visual is for our executive team and should be extremely easy to read with engaging visuals for the stats included. Please include a cover page.

Target Market(s)

Corporate Executive Team

Industry/Entity Type

Senior Housing

Other font styles liked:
• Canada Type Gibson

Colors
0054AA
0677BA
7BADD7
CADEEF
E8F1F8

Requirements
Must have
• QVN branding, include all information on provided doc

```html
<!DOCTYPE html>
<html lang="en">
<head>
<meta charset="utf-8">
<title>Maplers Report – Senior Care REIT</title>
<link href="https://fonts.googleapis.com/css2?family=Figtree:wght@300;400;600;700&display=swap" rel="stylesheet">
<style>
:root{
  --canvas:#9a9a9a;
  --white:#ffffff;
  --ink:#111111;
  --navy:#0b318f;
  --blue:#0054aa;
  --mid:#1f5fb8;
  --sky:#0677ba;
  --light:#7badd7;
  --pale:#cadeef;
  --mist:#e8f1f8;
  --black:#000000;
}
*{margin:0;padding:0;box-sizing:border-box}
html,body{width:843px;height:1200px;overflow:hidden}
body{background:var(--canvas);font-family:"Figtree",sans-serif;color:var(--ink);position:relative}
.slide{position:absolute;width:385px;height:217px;background:var(--white);overflow:hidden}
.c1{left:29px}.c2{left:429px}
.r1{top:29px}.r2{top:260px}.r3{top:491px}.r4{top:722px}.r5{top:953px}
.photo{position:absolute;top:0;bottom:0}
.footer{position:absolute;left:0;right:0;bottom:0;height:11px;background:var(--black);color:var(--white);
  font-size:5.6px;letter-spacing:1.1px;text-align:center;line-height:11px;font-weight:400}
.footer.blue{background:var(--navy)}
.footer.gradient{background:linear-gradient(90deg,var(--light),var(--sky) 50%,var(--navy))}
.footer .mark{position:absolute;right:8px;top:0;font-weight:700;font-size:6px;letter-spacing:.3px}
.brand{position:absolute;display:flex;align-items:center;gap:5px;font-weight:700;color:var(--navy);font-size:19px;letter-spacing:.5px}
.brand .sq{width:14px;height:14px;background:var(--navy)}
.brand.light{color:var(--white)}.brand.light .sq{background:var(--white)}
.bullet-title{display:flex;align-items:center;gap:7px;font-weight:600;font-size:17px;color:var(--ink)}
.bullet-title::before{content:"";width:11px;height:11px;background:var(--navy);transform:rotate(45deg)}
.body{font-size:8.8px;line-height:1.32;font-weight:300}
.body b{font-weight:600}
.callout{position:absolute;background:var(--mid);color:var(--white);font-weight:600;font-size:7.6px;line-height:1.35;padding:7px 10px}
.list{list-style:none;font-size:7px;line-height:1.22;font-weight:300}
.list li{position:relative;padding-left:6px;margin-bottom:2.4px}
.list li::before{content:"›";position:absolute;left:0;top:-1px;color:var(--blue);font-weight:700}
.list b{font-weight:600}
.heading{font-weight:600;font-size:7.6px;line-height:1.3}

/* cover */
.cover{background:linear-gradient(160deg,#222a37,#10151e 70%)}
.cover .title{position:absolute;left:0;right:0;top:117px;text-align:center;color:var(--white);font-weight:600;font-size:13px;line-height:1.25}
.cover .rule{position:absolute;left:137px;width:111px;top:153px;height:1.5px;background:var(--light)}
.cover .rule::before,.cover .rule::after{content:"";position:absolute;top:-1px;width:3px;height:3px;background:var(--light)}
.cover .rule::after{right:0}
.cover .reit{position:absolute;left:0;right:0;top:154px;text-align:center;color:var(--white);font-weight:700;font-size:42px;letter-spacing:1px}

/* group intro */
.groups{position:absolute;left:26px;top:91px;width:162px}
.groups .tag{display:flex;align-items:center;gap:6px;font-weight:400;font-size:9.4px;margin-top:5.5px}
.groups .tag::before{content:"";width:7px;height:7px;background:var(--navy);transform:rotate(45deg)}

/* closing */
.closing{background:linear-gradient(135deg,var(--mist),var(--white) 60%,var(--mist))}
.stat{position:absolute;top:104px;width:106px;height:87px;color:var(--white);font-size:8.4px;line-height:1.34;padding:7px 8px;font-weight:300}
.stat b{font-weight:600}
</style>
</head>
<body>

<!-- Cover -->
<section class="slide c1 r1 cover">
  <div class="photo" style="left:0;right:0;background:linear-gradient(180deg,#2a3342,#141a24)" role="img" aria-label="Dusk exterior of a senior living residence, darkened"></div>
  <div class="brand light" style="left:142px;top:44px"><span class="sq"></span>QVN REIT</div>
  <div class="title">Maplers Report<br>Senior Care</div>
  <div class="rule"></div>
  <div class="reit">REIT</div>
  <div class="footer gradient">COPYRIGHT 2024 - QVN REIT</div>
</section>

<!-- Categories -->
<section class="slide c2 r1">
  <div class="brand" style="left:26px;top:45px"><span class="sq"></span>QVN REIT</div>
  <div class="groups">
    <p class="body"><b>Respondents were categorized</b> in one of three groups based on their likelihood of moving to an <b>age-qualified community</b> in the future:</p>
    <div class="tag" style="margin-top:9px">PROBABLES</div>
    <div class="tag">POSSIBLES</div>
    <div class="tag">IMPROBABLES</div>
  </div>
  <div class="photo" style="left:200px;right:0;background:linear-gradient(180deg,#b98a8f,#7a5a5c 45%,#5b4e4c)" role="img" aria-label="Senior care center entrance at sunset"></div>
  <div class="footer">COPYRIGHT 2024 - QVN REIT</div>
</section>

<!-- Probables -->
<section class="slide c1 r2">
  <div class="brand" style="left:26px;top:28px"><span class="sq"></span>QVN REIT</div>
  <div class="bullet-title" style="position:absolute;left:26px;top:84px">PROBABLES</div>
  <p class="body" style="position:absolute;left:26px;top:111px;width:138px">Respondents who were likely or very likely to move to a residential community with services where the permanent residents must be a minimum of 55 years of age.</p>
  <div class="photo" style="left:185px;right:0;background:linear-gradient(135deg,#d8d2c8,#8b7a66 55%,#4a4440)" role="img" aria-label="Lobby with a vase of greenery on a round table"></div>
  <div class="footer">COPYRIGHT 2024 - QVN REIT</div>
</section>

<!-- Possibles -->
<section class="slide c2 r2">
  <div class="brand" style="left:26px;top:28px"><span class="sq"></span>QVN REIT</div>
  <div class="bullet-title" style="position:absolute;left:26px;top:84px">POSSIBLES</div>
  <p class="body" style="position:absolute;left:26px;top:111px;width:96px">Respondents who were unsure if they would move to a residential community where the permanent residents must be a minimum of 55 years of age.</p>
  <div class="photo" style="left:164px;right:0;background:linear-gradient(180deg,#b9cfe6,#8ea4bd 50%,#6f8d5a)" role="img" aria-label="Covered entrance of a senior residence with lawn"></div>
  <div class="footer">COPYRIGHT 2024 - QVN REIT</div>
</section>

<!-- Improbables -->
<section class="slide c1 r3">
  <div class="brand" style="left:26px;top:28px"><span class="sq"></span>QVN REIT</div>
  <div class="bullet-title" style="position:absolute;left:26px;top:84px">IMPROBABLES</div>
  <p class="body" style="position:absolute;left:26px;top:111px;width:94px">Respondents who were unlikely or very unlikely to move to a residential community where the permanent residents must be a minimum of 55 years of age</p>
  <div class="photo" style="left:185px;right:0;background:linear-gradient(160deg,#cfc3b0,#8a7560 50%,#6d7480)" role="img" aria-label="Sitting room with timber beams and patterned rug"></div>
  <div class="footer">COPYRIGHT 2024 - QVN REIT</div>
</section>

<!-- Top in-unit amenities -->
<section class="slide c2 r3">
  <div class="photo" style="left:0;width:193px;background:linear-gradient(180deg,#c9ccd0,#7a6a5c 55%,#4b3a30)" role="img" aria-label="Lounge with a round wooden table and ceramic vase"></div>
  <p style="position:absolute;left:204px;top:22px;width:162px;font-size:7px;line-height:1.35;font-weight:300">The top five in-unit amenities ranked by all respondents were full kitchen (refrigerator, stove/oven, microwave); laundry room with washer/dryer; living room or great room; lots of windows for plenty of natural light; and additional storage space for seasonal or occasionally used items.</p>
  <p class="heading" style="position:absolute;left:204px;top:93px;width:160px">Most preferred location among Probables and Possibles:</p>
  <div class="callout" style="left:138px;top:119px;width:222px">Outlying suburban (outer edge developed areas of a city where there are more single-family homes and neighborhoods and fewer commercial areas) (43%)</div>
  <div class="footer blue">COPYRIGHT 2024 - QVN REIT<span class="mark">QVN</span></div>
</section>

<!-- Essential in-unit -->
<section class="slide c1 r4">
  <p class="heading" style="position:absolute;left:23px;top:22px;width:150px">59% of Probables &amp; Possibles rated the following as essential or desirable:</p>
  <ul class="list" style="position:absolute;left:23px;top:46px;width:150px">
    <li>Full kitchen with refrigerator, stove/oven and microwave</li>
    <li>Laundry room with washer/dryer</li>
    <li>Living room or great room</li>
    <li>Lots of windows for plenty of natural light</li>
    <li>Additional storage space for seasonal or occasionally used items</li>
    <li>Fiber-Optic Internet/Gigabit Internet</li>
    <li>Walk-in closet</li>
    <li>Open porch, patio, or balcony</li>
    <li>Dining area in the kitchen</li>
    <li>Screened porch, patio, or balcony</li>
    <li>Study or den</li>
    <li>Enclosed porch, patio, or balcony</li>
  </ul>
  <div class="photo" style="left:185px;right:0;background:linear-gradient(180deg,#3f6fb2,#2f4a72 45%,#6d6a66)" role="img" aria-label="Blue-sided residence with stone facade"></div>
  <div class="callout" style="left:163px;top:123px;width:154px;font-size:7.4px">55% and 61% of Probables and Possibles, respectively, would prefer to receive care “In my residence”</div>
  <div class="footer blue">COPYRIGHT 2024 - QVN REIT<span class="mark">QVN</span></div>
</section>

<!-- Common area amenities -->
<section class="slide c2 r4">
  <div class="photo" style="left:0;width:135px;background:linear-gradient(180deg,#1f6cc2,#5e8fc8 45%,#b9b3a8)" role="img" aria-label="Multi-storey residence under a blue sky"></div>
  <p class="heading" style="position:absolute;left:154px;top:22px;width:210px">“Desirable + essential” preferences for common area amenities among Probables &amp; Possibles:</p>
  <ul class="list" style="position:absolute;left:154px;top:51px;width:102px">
    <li><b>Walking trails 64%</b></li>
    <li><b>On-site storage units 55%</b></li>
    <li><b>Indoor fitness center 54%</b></li>
    <li><b>Activity room 52%</b></li>
    <li><b>Convenience store 52%</b></li>
    <li><b>A family-friendly lounge 52%</b></li>
    <li><b>ATM 50%</b></li>
    <li>Multi-purpose room: group meetings, classes, card room, etc. 49%</li>
  </ul>
  <ul class="list" style="position:absolute;left:262px;top:51px;width:102px">
    <li>Library 47%</li>
    <li>Indoor swimming pool 46%</li>
    <li>Beauty salon/barbershop 45%</li>
    <li>Visiting doctor's clinic 42%</li>
    <li>Indoor running/walking track 41%</li>
    <li>Media room/movie room 41%</li>
    <li>Outdoor grilling stations 40%</li>
  </ul>
  <div class="footer blue">COPYRIGHT 2024 - QVN REIT<span class="mark">QVN</span></div>
</section>

<!-- By age group -->
<section class="slide c1 r5">
  <p class="heading" style="position:absolute;left:18px;top:22px;width:215px">“Desirable + essential” preferences for common area amenities among Probables &amp; Possibles broken up by age group (55-74 – 75+):</p>
  <ul class="list" style="position:absolute;left:18px;top:57px;width:118px">
    <li><b>Walking trails 67% – 59%</b></li>
    <li><b>Indoor fitness center 55% – 52%</b></li>
    <li><b>On-site storage units 54% – 56%</b></li>
    <li><b>Activity room 52% – 52%</b></li>
    <li><b>ATM 51% – 48%</b></li>
    <li><b>Convenience store 51% – 52%</b></li>
    <li>A family-friendly lounge 49% – 56%</li>
    <li>Indoor swimming pool 48% – 42%</li>
    <li>Multi-purpose room: group meetings, classes, card room, etc. 47% – 51%</li>
  </ul>
  <ul class="list" style="position:absolute;left:141px;top:57px;width:98px">
    <li>Outdoor grilling stations 45% – 34%</li>
    <li>Library 44% – 51%</li>
    <li>Outdoor swimming pool 44% – 30%</li>
    <li>Beauty salon/barbershop 43% – 49%</li>
    <li>Indoor running/walking track 43% – 38%</li>
    <li>Visiting doctor's clinic 42% – 42%</li>
  </ul>
  <div class="photo" style="left:244px;right:0;background:linear-gradient(180deg,#c9ccd0,#7a6a5c 55%,#4b3a30)" role="img" aria-label="Lounge with a round wooden table and ceramic vase"></div>
  <div class="footer blue">COPYRIGHT 2024 - QVN REIT<span class="mark">QVN</span></div>
</section>

<!-- Lifestyle stats -->
<section class="slide c2 r5 closing">
  <div class="brand" style="left:147px;top:44px"><span class="sq"></span>QVN REIT</div>
  <div class="stat" style="left:23px;background:var(--navy)">29% of Possibles &amp; Probables considered it essential and 35% considered themselves indifferent to having a pet-friendly community</div>
  <div class="stat" style="left:139px;background:var(--mid)">69% of Possibles &amp; Probables prefer Dining Out as a desired activity <b>(community proximity to restaurants is a must)</b></div>
  <div class="stat" style="left:256px;background:#5c9fd8">58% of Possibles &amp; Probables desire local travel as a possible activity (47% desire travel US &amp; abroad)</div>
  <div class="footer blue">COPYRIGHT 2024 - QVN REIT<span class="mark">QVN</span></div>
</section>

</body>
</html>
```